Tovlen Systems New Website - IT Infrastructure | Smart Cabinet | Micro Data Center

We're an IT SI providing Server Room Design & Build | All-in-One Rack & Smart Cabinet | Structured Cabling | IT Relocation | Maintenance. Old website can be found at www.tovlensys.com.hk. We'd like a brand new wix website which is modern, minimalist, interactive with some animation. Website content will be mostly static and include our service, our project, news and events, about us, contacts, blogs, partners and brands, etc.

reference sites:
We'd like to see more designs referring to below

https://www.pixelbazar.example/design/51730264
https://www.pixelbazar.example/design/51869047
https://vellhorn.example/

Animation (scrolling effect) referring to
https://vellhorn.example/intelligence/smart-office-room/
Updates

we'd like below style.

Designs look the same

Target Market(s)

Commercials in HK

Industry/Entity Type

IT, Technology, Data Center

Coding

Coded - Design and coding required

Font styles to use
Sans Serif

Requirements
Must have
• CMS, Some Interactive Elements/ Graphics

```html
<!DOCTYPE html>
<html lang="en">
<head>
<meta charset="utf-8">
<title>Tovlen Systems</title>
<link href="https://fonts.googleapis.com/css2?family=Poppins:wght@300;400;500;600&family=Cinzel:wght@600&display=swap" rel="stylesheet">
<style>
:root{
  --red:#e2261c;
  --red-deep:#cf2a1f;
  --black:#0b0b0b;
  --ink:#222;
  --grey-text:#555;
  --light:#f3f3f3;
  --white:#fff;
  --blue:#2a7fd4;
}
*{box-sizing:border-box;margin:0;padding:0}
html,body{width:1200px;height:4815px;overflow:hidden}
body{font-family:"Poppins",sans-serif;color:var(--ink);background:var(--white);position:relative}
section,header,footer{position:absolute;left:0;width:1200px}
.abs{position:absolute}
.btn-red{position:absolute;background:var(--red);color:#fff;font-size:15px;display:flex;align-items:center;justify-content:center}
.btn-outline{position:absolute;border:1.5px solid var(--red);color:var(--red);font-size:14px;display:flex;align-items:center;justify-content:center;background:#fff}
.section-title{position:absolute;left:0;width:1200px;text-align:center;color:var(--red);font-size:50px;font-weight:400}

/* header */
.site-header{top:0;height:131px;background:var(--black)}
.brand{left:88px;top:34px;display:flex;align-items:center;gap:14px;color:#fff;font-size:38px;font-weight:500}
.brand-mark{width:40px;height:40px;border:3px solid #fff}
.nav{left:468px;top:52px;display:flex;gap:24px;color:#fff;font-size:15px}
.nav .active{color:var(--red);border-bottom:2px solid var(--red);padding-bottom:4px}
.header-cta{left:996px;top:47px;width:120px;height:38px;font-size:15px}

/* hero */
.hero{top:131px;height:630px;background:linear-gradient(180deg,#2d7fcf 0%,#2a86dc 60%,#3c92e0 100%)}
.hero-photo{left:0;top:0;width:520px;height:630px;background:linear-gradient(135deg,#1d5fa6 0%,#2c75bf 60%,#2a7fd4 100%)}
.hero-title{left:538px;top:182px;font-family:"Cinzel",serif;color:#fff;font-size:52px;font-weight:600;letter-spacing:1px}
.hero-text{left:540px;top:266px;width:580px;color:#fff;font-size:15.5px;line-height:23px}
.hero-btn{left:536px;top:386px;width:146px;height:46px}

/* partners */
.partners{top:761px;height:122px;background:#fff}
.arrow-btn{top:47px;width:20px;height:34px;border:1.5px solid var(--red);border-radius:4px}
.partner-row{left:142px;top:40px;width:920px;display:flex;justify-content:space-between;align-items:center;height:48px;font-size:28px;font-weight:600;color:#333}

/* services */
.services{top:883px;height:645px;background:var(--light)}
.services .section-title{top:40px}
.card{top:132px;width:245px;height:427px;background:#fff;box-shadow:0 2px 6px rgba(0,0,0,.08)}
.card.raised{box-shadow:0 4px 14px rgba(0,0,0,.2)}
.card-photo{position:absolute;left:4px;top:4px;width:237px;height:140px}
.card-title{position:absolute;left:10px;width:225px;top:170px;text-align:center;color:var(--red);font-size:17px;line-height:24px}
.card-text{position:absolute;left:14px;width:217px;top:234px;text-align:center;color:var(--grey-text);font-size:13px;line-height:20px}
.card .btn-outline{left:52px;top:344px;width:145px;height:34px}
.card .btn-red{left:52px;top:344px;width:145px;height:34px;font-size:14px}

/* about */
.about{top:1528px;height:519px;background:#fff}
.about-photo{left:86px;top:82px;width:454px;height:353px;background:linear-gradient(135deg,#cfd8de 0%,#9aa7b0 50%,#e6e2dc 100%)}
.about-title{left:580px;top:108px;color:var(--red);font-size:28px;font-weight:500}
.about-text{left:580px;top:164px;width:520px;color:var(--grey-text);font-size:15px;line-height:22px}
.about-text p+p{margin-top:22px}
.about-btn{left:580px;top:356px;width:147px;height:38px}

/* projects */
.projects{top:2047px;height:1041px;background:var(--light)}
.projects .section-title{top:58px}
.tile{position:absolute}
.tile-overlay{background:var(--red);color:#fff;text-align:center}
.tile-overlay h3{position:absolute;top:110px;width:100%;font-size:21px;font-weight:400}
.tile-overlay p{position:absolute;top:156px;left:22px;width:255px;font-size:15px;line-height:22px}

/* contact band */
.touch{top:3088px;height:348px;background:linear-gradient(90deg,#121212,#1d1d1d 50%,#121212)}
.touch h2{position:absolute;top:62px;width:100%;text-align:center;color:#fff;font-size:52px;font-weight:500}
.touch p{position:absolute;left:196px;top:158px;width:808px;text-align:center;color:#fff;font-size:15px;line-height:22px}
.touch-btn{left:503px;top:241px;width:194px;height:49px;border:1.5px solid #fff;color:#fff;font-size:19px;display:flex;align-items:center;justify-content:center}

/* news */
.news{top:3436px;height:856px;background:#fff}
.news .section-title{top:62px}
.news-main{left:88px;top:207px;width:495px;height:494px;background:#fff;box-shadow:0 2px 10px rgba(0,0,0,.1)}
.news-main .photo{position:absolute;left:0;top:0;width:495px;height:245px;background:linear-gradient(135deg,#8b9298,#d5d8da 60%,#a7adb1)}
.news-date{color:#444;font-size:14px}
.news-main .news-date{position:absolute;left:18px;top:278px}
.news-main h3{position:absolute;left:18px;top:312px;width:440px;color:var(--red);font-size:18px;font-weight:400;line-height:28px}
.news-main p{position:absolute;left:18px;top:376px;width:440px;color:#444;font-size:14.5px;line-height:21px}
.news-item{left:600px;width:518px;height:140px;background:#fff;box-shadow:0 2px 10px rgba(0,0,0,.1)}
.news-item .photo{position:absolute;left:0;top:0;width:212px;height:140px}
.news-item .news-date{position:absolute;left:240px;top:18px;font-size:13.5px}
.news-item h3{position:absolute;left:240px;top:44px;color:var(--red);font-size:18px;font-weight:400}
.news-item p{position:absolute;left:240px;top:74px;width:260px;color:#444;font-size:14.5px;line-height:21px}
.news-more{left:512px;top:740px;width:172px;height:48px;font-size:20px}

/* footer */
.site-footer{top:4292px;height:523px;background:var(--red-deep);color:#fff}
.foot-brand{left:170px;top:172px;display:flex;align-items:center;gap:14px;font-size:48px;font-weight:500}
.foot-brand .brand-mark{width:52px;height:52px}
.socials{left:198px;top:265px;display:flex;gap:16px}
.socials span{width:36px;height:36px;border:2px solid #fff;border-radius:50%}
.foot-head{top:130px;font-size:19px;font-weight:600}
.quick{left:532px;top:198px;font-size:15px;line-height:31px;list-style:none}
.quick li::before{content:"›";margin-right:10px}
.foot-news-text{left:784px;top:198px;width:260px;font-size:15px;line-height:21px}
.foot-input{left:784px;top:256px;width:250px;height:37px;background:#fff}
.foot-sub{left:784px;top:308px;width:126px;height:38px;border:1.5px solid #fff;font-size:13px;display:flex;align-items:center;justify-content:center}
.foot-rule{left:90px;top:402px;width:1030px;height:1px;background:rgba(255,255,255,.6)}
.copyright{top:440px;width:100%;text-align:center;font-size:15px}
</style>
</head>
<body>

<header class="site-header">
  <div class="abs brand"><span class="brand-mark"></span>Tovlen</div>
  <nav class="abs nav">
    <span class="active">Home</span><span>About Us</span><span>Our Services</span><span>Our Projects</span><span>Testimonials</span>
  </nav>
  <div class="btn-red header-cta">Contact Us</div>
</header>

<section class="hero">
  <div class="abs hero-photo" role="img" aria-label="Security cameras mounted on a pole against blue sky"></div>
  <h1 class="abs hero-title">Tovlen Systems</h1>
  <p class="abs hero-text">Tovlen Systems is well experienced in delivering the best in Data Center Infrastructure, Network Infrastructure, Structured Cabling, Telephony, Relocation &amp; Migration and Maintenance solutions.</p>
  <div class="btn-red hero-btn">Read More</div>
</section>

<section class="partners">
  <svg class="abs arrow-btn" style="left:92px" viewBox="0 0 20 34"><path d="M12 12 L7 17 L12 22" fill="none" stroke="#e2261c" stroke-width="2"/></svg>
  <div class="abs partner-row">
    <span>CORVANE</span><span>HOLDTMANN</span><span style="font-style:normal">Kestrix</span><span style="color:#2bb673;font-weight:500">verdalo</span><span style="font-size:20px;font-weight:400;color:#2a4d8f">SONOMETRA</span>
  </div>
  <svg class="abs arrow-btn" style="left:1088px" viewBox="0 0 20 34"><path d="M8 12 L13 17 L8 22" fill="none" stroke="#e2261c" stroke-width="2"/></svg>
</section>

<section class="services">
  <h2 class="section-title">Our Services</h2>
  <div class="abs card" style="left:92px">
    <div class="card-photo" role="img" aria-label="Patch panel with network cables" style="background:linear-gradient(135deg,#1f4d5c,#4fa3b8 50%,#1c2c36)"></div>
    <div class="card-title">Data center design<br>and build</div>
    <div class="card-text">Data Center is like a brain to a business attention and tremendous resources from time to time.</div>
    <div class="btn-outline">Read More</div>
  </div>
  <div class="abs card" style="left:350px">
    <div class="card-photo" role="img" aria-label="Open office meeting room" style="background:linear-gradient(135deg,#e9ecec,#b9c36a 45%,#d8dcdc)"></div>
    <div class="card-title">Structured Cabling &amp;<br>Fiber Backbone</div>
    <div class="card-text">Heaps of office relocation, data center consolidation, business unit migration happen every week.</div>
    <div class="btn-outline">Read More</div>
  </div>
  <div class="abs card raised" style="left:606px">
    <div class="card-photo" role="img" aria-label="Ceiling-mounted cable trays" style="background:linear-gradient(135deg,#c9cbcc,#eeeeee 50%,#a9adb0)"></div>
    <div class="card-title">All-In-One Rack /<br>Micro-Data Center</div>
    <div class="card-text">All the components contained inside a Data Center are all critical facilities</div>
    <div class="btn-red">Read More &nbsp;›</div>
  </div>
  <div class="abs card" style="left:864px">
    <div class="card-photo" role="img" aria-label="Glass-walled conference room" style="background:linear-gradient(135deg,#3a2a24,#9a5a3a 50%,#d9d4cf)"></div>
    <div class="card-title">Audiovisual &amp; Conference<br>Room</div>
    <div class="card-text">In Tovlen Systems, you are able to focus your efforts in daily operation duties</div>
    <div class="btn-outline">Read More</div>
  </div>
</section>

<section class="about">
  <div class="abs about-photo" role="img" aria-label="Two colleagues reviewing a laptop in an office"></div>
  <h2 class="abs about-title">ABOUT TOVLEN SYSTEMS</h2>
  <div class="abs about-text">
    <p>Tovlen Systems is well experienced in delivering the best in Data Center professionalism that they deserved.</p>
    <p>Business needs with unbiased recommendation, but we also help IT Professionals create the most cost-effective solution and best uptime that meets their ever<br>changing demand.</p>
  </div>
  <div class="btn-red about-btn">Read More</div>
</section>

<section class="projects">
  <h2 class="section-title">Our Projects</h2>
  <div class="tile" role="img" aria-label="Technician working on server hardware" style="left:142px;top:174px;width:299px;height:290px;background:linear-gradient(135deg,#8d7a6a,#d7d7d7 60%,#9a9da0)"></div>
  <div class="tile tile-overlay" style="left:142px;top:473px;width:299px;height:452px">
    <h3>Design / Build</h3>
    <p>Data Center is like a brain to a business deserving and demanding top-level attention and tremendous resources from time to time.</p>
  </div>
  <div class="tile" role="img" aria-label="Fire extinguisher against a white wall" style="left:451px;top:174px;width:299px;height:452px;background:linear-gradient(180deg,#e5e6e6,#cfd1d2)"></div>
  <div class="tile" role="img" aria-label="Hands crimping network cables" style="left:451px;top:636px;width:299px;height:289px;background:linear-gradient(135deg,#dfe5ea,#5b8ec4 50%,#3d4a57)"></div>
  <div class="tile" role="img" aria-label="Blue server cabinet door" style="left:759px;top:174px;width:299px;height:290px;background:linear-gradient(135deg,#0d4fa0,#1f7ad6 60%,#0b3d80)"></div>
  <div class="tile" role="img" aria-label="Wall-mounted wiring panel" style="left:759px;top:473px;width:299px;height:452px;background:linear-gradient(90deg,#2f4a38 0%,#3d5a45 45%,#e6e6e4 55%,#d5d5d3 100%)"></div>
</section>

<section class="touch">
  <h2>Get In Touch</h2>
  <p>Tovlen Systems is well experienced in delivering the best in Data Center Infrastructure, Network Infrastructure, StrucAudiovisual &amp; Conferencing, Relocation &amp; Migration and Maintenance solutions.</p>
  <div class="abs touch-btn">CONTACT US</div>
</section>

<section class="news">
  <h2 class="section-title">Latest News</h2>
  <article class="abs news-main">
    <div class="photo" role="img" aria-label="Engineer servicing equipment in a plant room"></div>
    <div class="news-date">Mon 09 , 11 , 2020</div>
    <h3>Our expert IT staff have &nbsp;years of experience important IT specialties</h3>
    <p>We're proud of the great culture we've developed here, combines professionalism, a friendly face, communications &nbsp;our own.</p>
  </article>
  <article class="abs news-item" style="top:220px">
    <div class="photo" role="img" aria-label="Team working outdoors" style="background:linear-gradient(135deg,#5d6f80,#c8cfd4 60%,#3f4a52)"></div>
    <h3 style="top:34px">Important IT specialties</h3>
    <p style="top:64px">We're proud of the great culture developed ,within our own.</p>
  </article>
  <article class="abs news-item" style="top:383px">
    <div class="photo" role="img" aria-label="Fibre optic patch cables" style="background:linear-gradient(135deg,#1e6c86,#7fc3d2 50%,#e0a94a)"></div>
    <div class="news-date">Mon 09 , 11 , 2020</div>
    <h3>Important IT specialties</h3>
    <p>We're proud of the great culture developed ,within our own.</p>
  </article>
  <article class="abs news-item" style="top:546px">
    <div class="photo" role="img" aria-label="Colleagues in a meeting" style="background:linear-gradient(135deg,#3b3f45,#c9c2bd 55%,#8a8f94)"></div>
    <div class="news-date">Mon 09 , 11 , 2020</div>
    <h3>Important IT specialties</h3>
    <p>We're proud of the great culture developed ,within our own.</p>
  </article>
  <div class="btn-red news-more">View More</div>
</section>

<footer class="site-footer">
  <div class="abs foot-brand"><span class="brand-mark" style="border-color:#fff"></span>Tovlen</div>
  <div class="abs socials" aria-label="Social links"><span></span><span></span><span></span><span></span></div>
  <div class="abs foot-head" style="left:525px">Quick Links</div>
  <ul class="abs quick"><li>Home</li><li>About Us</li><li>Our Services</li><li>Our Blogs</li><li>Testimonials</li></ul>
  <div class="abs foot-head" style="left:784px">Our Newsletter</div>
  <p class="abs foot-news-text">Subscribe our newsletter to get the latest news.</p>
  <div class="abs foot-input"></div>
  <div class="abs foot-sub">SUBSCRIBE</div>
  <div class="abs foot-rule"></div>
  <div class="abs copyright">All Rights Reserved @ Copyrights 2023</div>
</footer>

</body>
</html>
```